E-learning Information & Community Website Needs a Makeover

I'm looking for a design makeover for my website "TavenNest.club". TavenNest's aim is to connect people to online learning through forums, information, guides & independent reviews. The site was launched in September 2014 using a forum software (Xenforo), but now needs a more polished and sophisticated look which communicates expertise and professionalism. I would like to see designs that use the current "TavenNest" blue (#0070c0). To visit the current website, go to http://www.tavennest.club/

Target Market(s)

People wishing to study online

Industry/Entity Type

Club

Number of Pages Required

4 page

Font styles to use
Sans Serif

Requirements
Must have
• A simple, clear and sophisticated lading page with links to the site's key features: discussion forums, Useful resources, Reviews, News etc, Articles. (See layout idea file attached)
• The main pages are the Landing Page, Discussion Forums, Resources & Reviews
• I would like to see designs that use the current "TavenNest" blue (#0070c0).
Nice to have
• Something uncluttered and easy to understand. The design should convey expertise in the field of online learning, giving users a sense of trust in the site's offerings.
• To give an idea of the sort of thing I'm after, take a look at brimvale.com website (screenshot attached)

```html
<!DOCTYPE html>
<html lang="en">
<head>
<meta charset="utf-8">
<title>TavenNest — Connecting People to Online Learning</title>
<link rel="stylesheet" href="https://fonts.googleapis.com/css2?family=Open+Sans:wght@300;400;600;700&display=swap">
<style>
:root{
  --brand:#0070c0;
  --brand-soft:#4f93d6;
  --link:#1f93dc;
  --ink:#333;
  --muted:#9a9a9a;
  --page:#efefef;
  --panel:#ffffff;
  --line:#d9d9d9;
  --bar:#0d0d0d;
  --sky-top:#8cc3ea;
  --sky-low:#d9ecf8;
}
*{box-sizing:border-box;margin:0;padding:0}
html,body{width:1130px;height:1200px;overflow:hidden}
body{font-family:"Open Sans",Arial,sans-serif;background:var(--page);color:var(--ink);position:relative}
a{text-decoration:none;color:inherit}

.hero{position:absolute;left:0;top:0;width:1130px;height:283px;background:linear-gradient(180deg,var(--sky-top),var(--sky-low))}
.hero-photo{position:absolute;left:380px;top:0;width:545px;height:283px;background:linear-gradient(135deg,#c9dbe8 0%,#e3a36a 35%,#3bb3c3 60%,#9fd18a 85%,#c9dbe8 100%);opacity:.85}
.brand-box{position:absolute;left:215px;top:0;width:173px;height:78px;background:var(--brand);color:#fff;padding:26px 10px 0}
.brand-name{font-size:21px;font-weight:400;line-height:1}
.brand-tag{font-size:9px;font-weight:600;margin-top:6px}
.brand-pitch{position:absolute;left:215px;top:78px;width:173px;height:100px;background:var(--brand-soft);color:#fff;padding:15px 14px;font-size:16px;line-height:21px;font-weight:400}
.brand-pitch strong{font-weight:600}

.main-nav{position:absolute;left:0;top:283px;width:1130px;height:30px;background:var(--bar)}
.main-nav ul{list-style:none;display:flex;position:absolute;left:215px;top:0;height:30px}
.main-nav li{font-size:10.5px;color:#8a8a8a;line-height:30px;padding:0 16px}
.main-nav li.active{background:var(--brand);color:#fff;padding:0 18px}

.features{position:absolute;left:0;top:313px;width:1130px;height:162px;background:var(--page);border-bottom:1px solid var(--line)}
.feature{position:absolute;width:228px;height:49px;background:var(--panel);border:1px solid var(--line);display:flex;align-items:center;padding-left:16px;font-size:13px;font-style:italic;color:#444}
.feature svg{width:28px;height:28px;margin-right:14px;flex:none}

.topics{position:absolute;left:0;top:475px;width:1130px;height:159px;background:var(--page);border-bottom:1px solid var(--line)}
.section-title{position:absolute;left:0;width:1130px;text-align:center;font-size:27px;font-weight:300;color:#222;letter-spacing:.5px}
.topics .section-title{top:28px}
.topic-strip{position:absolute;left:198px;top:84px;width:765px;height:69px;background:#f8f8f8;display:flex;align-items:center;justify-content:space-between;padding:0 22px}
.topic{font-size:15px;font-weight:600;color:#333}
.topic-mark{display:block;width:40px;height:40px;background:#333}
.topic-mark.round{border-radius:50%}
.topic-mark.square{width:27px;height:40px}

.community{position:absolute;left:0;top:634px;width:1130px;height:467px}
.community .section-title{top:36px}
.thread-head{position:absolute;left:212px;top:96px;width:708px;height:24px;border-bottom:1px solid var(--line);font-size:9.5px;color:#555;text-transform:uppercase}
.thread-head span{position:absolute;top:4px}
.threads{position:absolute;left:212px;top:132px;width:708px}
.thread{display:flex;align-items:center;background:var(--panel);border-bottom:2px solid var(--page);height:51px}
.thread.tall{height:55px}
.avatar{width:34px;height:34px;margin:0 9px 0 7px;flex:none;border-radius:3px;background:var(--brand);color:#fff;font-size:9px;line-height:11px;text-align:center;padding-top:7px}
.avatar.person{background:#9c7a62}
.avatar.blank{background:#e8e8e8;border-radius:50%}
.thread-main{width:375px;flex:none}
.thread-title{font-size:14px;color:var(--link);line-height:18px}
.tag{display:inline-block;font-size:11px;line-height:14px;padding:0 5px;border-radius:2px;margin-right:3px;vertical-align:1px;color:#222}
.tag.article{background:#e8181c;color:#fff}
.tag.courses{background:#f5a623}
.tag.news{background:#b5b5b5}
.tag.event{background:#8c8c8c}
.tag.advice{background:#8fdc7a}
.thread-meta{font-size:10px;color:var(--muted);line-height:14px}
.thread-stats{width:80px;margin-left:5px;border-left:1px solid var(--line);padding-left:8px;font-size:13px;color:var(--muted);position:relative;height:36px}
.thread-stats .lbl-r{position:absolute;left:8px;top:-2px}
.thread-stats .lbl-v{position:absolute;left:8px;top:18px;font-size:10px}
.thread-stats .num-r{position:absolute;right:4px;top:-2px;color:#333}
.thread-stats .num-v{position:absolute;right:4px;top:18px;font-size:10px;color:#333}
.thread-last{flex:1;text-align:right;padding-right:4px;border-left:1px solid var(--line);height:36px}
.thread-last .who{font-size:14px;color:var(--link);line-height:19px}
.thread-last .when{font-size:10px;color:var(--muted)}

.site-footer{position:absolute;left:0;top:1101px;width:1130px;height:99px;background:var(--bar)}
.footer-links{position:absolute;left:215px;top:27px;display:flex;list-style:none;font-size:9px;color:#ddd}
.footer-links li{margin-right:10px}
.newsletter{position:absolute;left:673px;top:16px;display:flex}
.newsletter span{width:186px;height:24px;background:#fff;font-size:10px;color:#333;padding:5px 10px}
.newsletter b{width:61px;height:24px;margin-left:3px;background:var(--brand);color:#fff;font-size:10px;font-weight:400;text-align:center;line-height:24px}
.social{position:absolute;left:519px;top:64px;display:flex}
.social i{width:18px;height:18px;border-radius:50%;margin-right:3px;background:#1c6fd1}
.social i:nth-child(3){background:#d9302b}
.social i:nth-child(4){background:#e04a3a}
</style>
</head>
<body>

<header class="hero">
  <div class="hero-photo" role="img" aria-label="Photo of four smiling students gathered around a laptop in front of a Paris skyline"></div>
  <div class="brand-box">
    <div class="brand-name">TavenNest</div>
    <div class="brand-tag">Connecting People to Online Learning</div>
  </div>
  <div class="brand-pitch">At the heart of connecting people <strong>to online learning</strong></div>
</header>

<nav class="main-nav">
  <ul>
    <li class="active">Home</li><li>Forums</li><li>Resources</li><li>Members</li><li>FAQ</li><li>Blog</li><li>TavenNest Español</li><li>Taven Scoop</li><li>Login</li>
  </ul>
</nav>

<section class="features">
  <a class="feature" style="left:215px;top:17px">
    <svg viewBox="0 0 28 28"><circle cx="14" cy="14" r="9" fill="none" stroke="#0070c0" stroke-width="5" stroke-dasharray="4 3"/><circle cx="14" cy="14" r="7" fill="#0070c0"/><circle cx="14" cy="14" r="3" fill="#fff"/></svg>Getting Started</a>
  <a class="feature" style="left:451px;top:17px">
    <svg viewBox="0 0 28 28"><circle cx="14" cy="14" r="13" fill="#0070c0"/><circle cx="8.5" cy="14" r="2" fill="#fff"/><circle cx="14" cy="14" r="2" fill="#fff"/><circle cx="19.5" cy="14" r="2" fill="#fff"/></svg>Discussions</a>
  <a class="feature" style="left:693px;top:17px">
    <svg viewBox="0 0 28 28"><path d="M2 14 Q14 3 26 14 Q14 25 2 14Z" fill="none" stroke="#0070c0" stroke-width="2.5"/><circle cx="14" cy="14" r="4" fill="#0070c0"/></svg>Reviews</a>
  <a class="feature" style="left:215px;top:87px">
    <svg viewBox="0 0 28 28"><path d="M8 26 L6 14 L6 8 Q8 7 9 8 L9 5 Q11 3 12 5 L12 3 Q14 2 15 4 L15 5 Q17 4 18 6 L18 13 L20 10 Q22 10 22 12 L19 22 L16 26Z" fill="#0070c0"/></svg>Tips &amp; Guidelines</a>
  <a class="feature" style="left:451px;top:87px">
    <svg viewBox="0 0 28 28"><circle cx="14" cy="14" r="11.5" fill="none" stroke="#0070c0" stroke-width="2.5"/><text x="14" y="18" font-size="10" font-weight="700" text-anchor="middle" fill="#0070c0" font-family="Open Sans,sans-serif">24</text></svg>News &amp; Articles</a>
  <a class="feature" style="left:693px;top:87px">
    <svg viewBox="0 0 28 28"><rect x="4" y="3" width="13" height="17" fill="#0070c0"/><rect x="10" y="8" width="13" height="17" fill="#fff" stroke="#0070c0" stroke-width="2.5"/><rect x="13" y="12" width="7" height="2" fill="#0070c0"/><rect x="13" y="17" width="7" height="2" fill="#0070c0"/></svg>Newsletter</a>
</section>

<section class="topics">
  <h2 class="section-title">FREQUENT TOPICS</h2>
  <div class="topic-strip">
    <span class="topic-mark round"></span>
    <span class="topic">Alderbank</span>
    <span class="topic">FERNLOW</span>
    <span class="topic">MARLOWE</span>
    <span class="topic">Halbrook</span>
    <span class="topic">RIDGELINE GLOBAL</span>
    <span class="topic-mark square"></span>
  </div>
</section>

<section class="community">
  <h2 class="section-title">FROM THE COMMUNITY</h2>
  <div class="thread-head">
    <span style="left:25px">Recent Threads</span>
    <span style="left:368px">Start Date</span>
    <span style="left:440px">Replies</span>
    <span style="left:538px">Views</span>
    <span style="left:580px">Last Message</span>
  </div>
  <div class="threads">
    <article class="thread tall">
      <div class="avatar person"></div>
      <div class="thread-main">
        <div class="thread-title"><span class="tag article">Article</span>Wellcom to UCLERx, the new catalan MOOC directory</div>
        <div class="thread-meta">JoanPere Vidal, Yesterday at 7:02 PM, Blog</div>
      </div>
      <div class="thread-stats"><span class="lbl-r">Replies:</span><span class="num-r">0</span><span class="lbl-v">Views:</span><span class="num-v">28</span></div>
      <div class="thread-last"><div class="who">JoanPere Vidal</div><div class="when">Yesterday at 7:02 PM</div></div>
    </article>
    <article class="thread">
      <div class="avatar">Taven<br>Nest</div>
      <div class="thread-main">
        <div class="thread-title"><span class="tag courses">Courses</span>Northwind MOOCs</div>
        <div class="thread-meta">Marion, Yesterday at 9:30 AM, edQuill</div>
      </div>
      <div class="thread-stats"><span class="lbl-r">Replies:</span><span class="num-r">0</span><span class="lbl-v">Views:</span><span class="num-v">55</span></div>
      <div class="thread-last"><div class="who">Marion</div><div class="when">Yesterday at 9:30 AM</div></div>
    </article>
    <article class="thread">
      <div class="avatar">Taven<br>Nest</div>
      <div class="thread-main">
        <div class="thread-title"><span class="tag news">News</span>TavenNest's Taven Scoop promoted to Gold level!</div>
        <div class="thread-meta">Marion, Monday at 6:24 PM, MOOC News</div>
      </div>
      <div class="thread-stats"><span class="lbl-r">Replies:</span><span class="num-r" style="color:#7a2c8c">1</span><span class="lbl-v">Views:</span><span class="num-v">47</span></div>
      <div class="thread-last"><div class="who">Radovan</div><div class="when">Tuesday at 2:14 PM</div></div>
    </article>
    <article class="thread">
      <div class="avatar">Taven<br>Nest</div>
      <div class="thread-main">
        <div class="thread-title"><span class="tag news">News</span>Kestrel Academy are looking for a video star!</div>
        <div class="thread-meta">Marion, Tuesday at 8:41 AM, General stuff on course providers</div>
      </div>
      <div class="thread-stats"><span class="lbl-r">Replies:</span><span class="num-r">0</span><span class="lbl-v">Views:</span><span class="num-v">116</span></div>
      <div class="thread-last"><div class="who">Marion</div><div class="when">Tuesday at 8:41 AM</div></div>
    </article>
    <article class="thread">
      <div class="avatar">Taven<br>Nest</div>
      <div class="thread-main">
        <div class="thread-title"><span class="tag event">Event</span>What Reviews divulge about Online Education</div>
        <div class="thread-meta">Marion, Monday at 10:52 AM, Events</div>
      </div>
      <div class="thread-stats"><span class="lbl-r">Replies:</span><span class="num-r">0</span><span class="lbl-v">Views:</span><span class="num-v">76</span></div>
      <div class="thread-last"><div class="who">Marion</div><div class="when">Monday at 10:52 AM</div></div>
    </article>
    <article class="thread tall">
      <div class="avatar blank"></div>
      <div class="thread-main">
        <div class="thread-title"><span class="tag advice">Advice</span>How do you "unenroll" from a course on Learnvia?</div>
        <div class="thread-meta">Helen, Feb 13, 2015, MOOC Advice</div>
      </div>
      <div class="thread-stats"><span class="lbl-r">Replies:</span><span class="num-r">2</span><span class="lbl-v">Views:</span><span class="num-v">3,482</span></div>
      <div class="thread-last"><div class="who">Owen</div><div class="when">Sunday at 11:01 PM</div></div>
    </article>
  </div>
</section>

<footer class="site-footer">
  <ul class="footer-links">
    <li>Home</li><li>Forums</li><li>Resources</li><li>Members</li><li>FAQ</li><li>Blog</li><li>TavenNest Español</li><li>Taven Scoop</li><li>Login</li>
  </ul>
  <div class="newsletter"><span>Subscribe for Monthly Newsletter</span><b>Subscribe</b></div>
  <div class="social"><i></i><i></i><i></i><i></i></div>
</footer>

</body>
</html>
```